Business card design needed for Varrick Medical Practice

We need a new design for our growing medical practice. Our previous design used blue, white and black. I would like to have a design with a baby, child, adult and grandparent on it. We look after a wide range of patients from newborns to 100 year olds.

Industry/Entity Type

Medical

Contact Information for Business Card

Varrick Medical Practice
14 Kestrel Rd Brindle Vale, NSW 2791
Ph 4812 6274 Fax 4831 9527
Dr Maud Pirelli Dr Beatrix Dunmore
Dr Yvonne Kaczmar Dr Estelle Whitcombe
Dr Tom Vasquillo Dr Rex Lund-Patmore
Open Mon- Fri 9-1, 2-5pm
Sat 9-12pm by appointment
web:www.varrickmedical.com.au
email:varrickmedical@quillpost.com

```html
<!DOCTYPE html>
<html lang="en">
<head>
<meta charset="utf-8">
<title>Varrick Medical Practice – Business Card</title>
<link rel="stylesheet" href="https://fonts.googleapis.com/css2?family=Tenor+Sans&display=swap">
<style>
  :root {
    --stage: #2b1721;
    --card-light: #ede1e8;
    --card-edge: #6e3a58;
    --ink-plum: #5b2a47;
    --ink-body: #3c2431;
    --divider: #7f7aa8;
    --card-dark-top: #3b1f2d;
    --card-dark-bottom: #21111a;
  }
  * { box-sizing: border-box; margin: 0; padding: 0; }
  html, body { width: 1200px; height: 1200px; overflow: hidden; }
  body {
    background: var(--stage);
    font-family: "Tenor Sans", sans-serif;
    position: relative;
  }
  .card {
    position: absolute;
    top: 330px;
    width: 370px;
    height: 540px;
    border-radius: 36px;
    overflow: hidden;
  }
  .card--front {
    left: 220px;
    background: var(--card-light);
    border-top: 12px solid var(--card-edge);
    color: var(--ink-body);
    padding: 52px 30px 0 30px;
  }
  .card--back {
    left: 630px;
    background: linear-gradient(160deg, var(--card-dark-top), var(--card-dark-bottom));
  }
  .brand {
    display: flex;
    align-items: center;
    gap: 12px;
  }
  .brand__name {
    font-size: 26px;
    color: var(--ink-plum);
  }
  .brand__dot {
    width: 40px;
    height: 40px;
    border-radius: 50%;
    background: var(--ink-plum);
  }
  .address {
    margin-top: 74px;
    font-size: 15px;
    line-height: 21px;
    padding-left: 6px;
  }
  .contacts {
    display: flex;
    margin-top: 20px;
    font-size: 15px;
    line-height: 23px;
    padding-left: 6px;
  }
  .doctors { list-style: none; width: 190px; }
  .phones {
    border-left: 2px dashed var(--divider);
    padding-left: 8px;
    height: 150px;
  }
  .hours { margin-top: 22px; font-size: 15px; padding-left: 6px; }
  .online {
    margin-top: 28px;
    font-size: 15px;
    line-height: 22px;
    padding-left: 6px;
  }
  .online__web { padding-left: 24px; }
  .back-brand {
    position: absolute;
    right: 28px;
    bottom: 86px;
    font-size: 30px;
    color: var(--card-light);
  }
</style>
</head>
<body>
  <section class="card card--front" aria-label="Business card front">
    <div class="brand">
      <span class="brand__name">Varrick Medical</span>
      <span class="brand__dot"></span>
    </div>
    <p class="address">Varrick Medical Practice<br>14 Kestrel Rd Brindle Vale, NSW 2791</p>
    <div class="contacts">
      <ul class="doctors">
        <li>Dr Maud Pirelli</li>
        <li>Dr Beatrix Dunmore</li>
        <li>Dr Yvonne Kaczmar</li>
        <li>Dr Estelle Whitcombe</li>
        <li>Dr Tom Vasquillo</li>
        <li>Dr Rex Lund-Patmore</li>
      </ul>
      <div class="phones">Ph 4812 6274<br>Fax 4831 9527</div>
    </div>
    <p class="hours">Open Mon- Fri 9-1, 2-5pm Sat 9-12pm</p>
    <p class="online">email:varrickmedical@quillpost.com<br><span class="online__web">www.varrickmedical.com.au</span></p>
  </section>

  <section class="card card--back" aria-label="Business card back">
    <span class="back-brand">Varrick Medical</span>
  </section>
</body>
</html>
```